Vemtra Group: Business Card for a high end technology company

We need a cool new design for our business cards using our cloud logo. We are a technology consulting business. We pride ourselves on be the best of the best. We mainly focus on cloud solutions and managed services. We need a business card that sets us apart from the other technology companies in the area and allows us to stand out.

Target Market(s)

Technology departments, CIO, CEOs, and Information Technology Staff.

Industry/Entity Type

Information Technology

Contact Information for Business Card

Must have the logo and our name.
Must have employee name, email address, office phone, cell phone and website.
Need to have all info on one side a cool design on backside.

Font styles to use
Serif
Sans Serif

Requirements
Must have
• Must have the logo and our name.
• Must have employee name, email address, office phone, cell phone and website.
• Need to have all info on one side a cool design on back side.
• Must be a crisp clean design, not too busy or confusing.

```html
<!DOCTYPE html>
<html lang="en">
<head>
<meta charset="utf-8">
<title>Vemtra Group Business Card</title>
<link href="https://fonts.googleapis.com/css2?family=Raleway:wght@400;600;700&display=swap" rel="stylesheet">
<style>
  :root {
    --canvas: #e9e9ea;
    --card-black: #1c1c1e;
    --card-black-soft: #3a3a3d;
    --card-white: #ffffff;
    --accent-blue: #1b9be0;
    --accent-blue-deep: #0b6fc0;
    --ink: #2b2b2e;
    --ink-light: #f2f2f2;
  }
  * { margin: 0; padding: 0; box-sizing: border-box; }
  html, body {
    width: 1200px; height: 796px; overflow: hidden;
    background: var(--canvas);
    font-family: "Raleway", Arial, sans-serif;
  }
  .canvas { position: relative; width: 1200px; height: 796px; }
  .card {
    position: absolute; width: 520px; height: 297px;
    overflow: hidden; border-radius: 3px;
    box-shadow: 0 10px 28px rgba(0,0,0,0.22);
  }
  .card-front { left: 50px; top: 110px; }
  .card-back { left: 630px; top: 390px; }
  .card-art { position: absolute; inset: 0; }
  .brand { position: absolute; display: flex; flex-direction: column; align-items: center; }
  .brand-row { display: flex; align-items: center; gap: 12px; }
  .brand-dot { width: 34px; height: 34px; border-radius: 50%; background: var(--accent-blue); }
  .brand-name { font-weight: 400; font-size: 34px; letter-spacing: 0.5px; }
  .brand-web { font-size: 11px; font-weight: 600; margin-top: 4px; letter-spacing: 0.4px; }
  .card-front .brand { left: 0; right: 0; top: 112px; color: var(--ink); }
  .card-back .brand { left: 20px; top: 150px; width: 270px; color: var(--ink-light); }
  .card-back .brand-name { font-size: 28px; }
  .contact { position: absolute; left: 318px; top: 36px; width: 190px; color: var(--ink); }
  .person-name { font-weight: 700; font-size: 22px; letter-spacing: 0.5px; text-transform: uppercase; }
  .person-title { font-size: 11px; color: var(--accent-blue); letter-spacing: 0.6px; text-transform: uppercase; margin-top: 2px; }
  .contact-list { list-style: none; margin-top: 22px; }
  .contact-item { display: flex; align-items: flex-start; gap: 10px; font-size: 11.5px; line-height: 1.45; margin-bottom: 10px; }
  .contact-icon { flex: none; width: 22px; height: 22px; }
</style>
</head>
<body>
<main class="canvas">

  <section class="card card-front" aria-label="Card front">
    <svg class="card-art" viewBox="0 0 520 297" width="520" height="297">
      <defs>
        <linearGradient id="frontBlack" x1="0" y1="0" x2="1" y2="1">
          <stop offset="0" stop-color="var(--card-black-soft)"/>
          <stop offset="1" stop-color="var(--card-black)"/>
        </linearGradient>
        <linearGradient id="frontBlue" x1="0" y1="0" x2="1" y2="1">
          <stop offset="0" stop-color="var(--accent-blue)"/>
          <stop offset="1" stop-color="var(--accent-blue-deep)"/>
        </linearGradient>
      </defs>
      <rect width="520" height="297" fill="url(#frontBlack)"/>
      <circle cx="262" cy="150" r="222" fill="url(#frontBlue)"/>
      <circle cx="262" cy="146" r="206" fill="var(--card-white)"/>
    </svg>
    <div class="brand">
      <div class="brand-row">
        <span class="brand-dot"></span>
        <span class="brand-name">Vemtra Group</span>
      </div>
      <span class="brand-web">www.vemtragroup.com</span>
    </div>
  </section>

  <section class="card card-back" aria-label="Card back">
    <svg class="card-art" viewBox="0 0 520 297" width="520" height="297">
      <defs>
        <linearGradient id="backBlack" x1="0" y1="0" x2="1" y2="1">
          <stop offset="0" stop-color="var(--card-black-soft)"/>
          <stop offset="1" stop-color="var(--card-black)"/>
        </linearGradient>
      </defs>
      <rect width="520" height="297" fill="url(#backBlack)"/>
      <circle cx="560" cy="120" r="276" fill="var(--accent-blue)"/>
      <circle cx="566" cy="114" r="264" fill="var(--card-white)"/>
    </svg>
    <div class="brand">
      <div class="brand-row">
        <span class="brand-dot"></span>
        <span class="brand-name">Vemtra Group</span>
      </div>
      <span class="brand-web">www.vemtragroup.com</span>
    </div>
    <div class="contact">
      <p class="person-name">Owen Hartley</p>
      <p class="person-title">Creative Director</p>
      <ul class="contact-list">
        <li class="contact-item">
          <svg class="contact-icon" viewBox="0 0 22 22"><circle cx="11" cy="11" r="11" fill="var(--accent-blue)"/><path d="M7 8c0-1 1-2 2-1l1 1.5c.3.5 0 1-.4 1.2.5 1.2 1.4 2.1 2.6 2.6.2-.4.7-.7 1.2-.4L15 13c1 1 0 2-1 2-3.5 0-7-3.5-7-7z" fill="#fff"/></svg>
          <span>555.014.2290</span>
        </li>
        <li class="contact-item">
          <svg class="contact-icon" viewBox="0 0 22 22"><circle cx="11" cy="11" r="11" fill="var(--accent-blue)"/><g fill="none" stroke="#fff" stroke-width="1.1"><circle cx="11" cy="11" r="5"/><ellipse cx="11" cy="11" rx="2.2" ry="5"/><path d="M6 11h10"/></g></svg>
          <span>hello@vemtragroup.com<br>www.vemtragroup.com</span>
        </li>
        <li class="contact-item">
          <svg class="contact-icon" viewBox="0 0 22 22"><circle cx="11" cy="11" r="11" fill="var(--accent-blue)"/><path d="M11 5a4 4 0 0 1 4 4c0 3-4 8-4 8s-4-5-4-8a4 4 0 0 1 4-4z" fill="#fff"/><circle cx="11" cy="9" r="1.5" fill="var(--accent-blue)"/></svg>
          <span>240 Linden Avenue<br>Suite 300<br>Marlow, GA 30000</span>
        </li>
      </ul>
    </div>
  </section>

</main>
</body>
</html>
```